Business card design needed

Want the logo on a medium blue background and a nice funky design. I have my own gym and run one on one personal training and nutrition sessions. want it to look lively.
Updates

Please note I requested my logo on a blue background 

PLEASE NOTE: I already have a logo. It is attached to the order!!

Target Market(s)

over 55s

Industry/Entity Type

Nutrition

Contact Information for Business Card

Front of card : Logo ( on blue background )
Corinne Dalby
Nutrition & Fitness Coach for Seniors
Private gym at : 17 Fennick Street, Brantwood, Perth, WA 6291
Mob : 0412736158
Email : corinnedalby@fernpost.example
"For Seniors by a Senior"

Back of card
B.A. ( Soc.)
Dip. Ed. (Sec.)
Wellness Coach
Cert 4 Personal Trainer
Cert. Nutritition
MOVE ON Facilitator
Ageing Well Moving Freely Facilitator
NLP Master

```html
<!DOCTYPE html>
<html lang="en">
<head>
<meta charset="utf-8">
<title>Corinne Dalby Nutrition &amp; Fitness – Business Card</title>
<link rel="stylesheet" href="https://fonts.googleapis.com/css2?family=Cormorant+Garamond:ital,wght@1,500;1,700&display=swap">
<style>
  :root {
    --page: #ffffff;
    --card-white: #ffffff;
    --sky: #9dd9ea;
    --teal: #1f7a8c;
    --ink: #222222;
    --script-ink: #3d3d3d;
    --brand-blue: #2f8fe8;
    --edge: #111111;
  }
  html, body {
    margin: 0;
    padding: 0;
    width: 1200px;
    height: 379px;
    overflow: hidden;
    background: var(--page);
  }
  .canvas {
    position: relative;
    width: 1200px;
    height: 379px;
  }
  .card {
    position: absolute;
    top: 33px;
    width: 535px;
    height: 310px;
    border: 1px solid var(--edge);
    border-radius: 18px;
    overflow: hidden;
    box-sizing: border-box;
  }
  .script {
    font-family: "Cormorant Garamond", "Georgia", serif;
    font-style: italic;
    font-weight: 500;
  }
  .plain {
    font-family: Arial, Helvetica, sans-serif;
    font-size: 14px;
    color: var(--ink);
    line-height: 17px;
  }

  /* Front */
  .card--front {
    left: 62px;
    background: var(--card-white);
  }
  .front__lower {
    position: absolute;
    left: 0;
    top: 152px;
    width: 100%;
    height: 158px;
    background: var(--sky);
    border-top: 1px solid var(--edge);
  }
  .front__wedge {
    position: absolute;
    left: 0;
    top: 93px;
  }
  .brand-mark {
    position: absolute;
    display: flex;
    align-items: center;
    gap: 8px;
    white-space: nowrap;
  }
  .brand-mark__dot {
    border-radius: 50%;
    background: var(--brand-blue);
    flex: none;
  }
  .brand-mark__name {
    font-family: "Cormorant Garamond", "Georgia", serif;
    font-style: italic;
    font-weight: 700;
  }
  .front__brand {
    left: 188px;
    top: 40px;
  }
  .front__brand .brand-mark__dot { width: 16px; height: 16px; }
  .front__brand .brand-mark__name { font-size: 24px; color: var(--teal); }

  .front__title {
    position: absolute;
    left: 101px;
    top: 118px;
    margin: 0;
    font-size: 28px;
    color: var(--script-ink);
    white-space: nowrap;
  }
  .front__role {
    position: absolute;
    right: 11px;
    top: 162px;
    margin: 0;
    font-size: 21px;
    color: var(--script-ink);
  }
  .front__gym {
    position: absolute;
    left: 320px;
    top: 200px;
    display: flex;
    gap: 8px;
  }
  .front__contact {
    position: absolute;
    left: 10px;
    top: 219px;
  }
  .front__tagline {
    position: absolute;
    left: 0;
    width: 100%;
    top: 276px;
    margin: 0;
    text-align: center;
    font-size: 20px;
    color: var(--script-ink);
  }

  /* Back */
  .card--back {
    left: 615px;
    background: var(--teal);
  }
  .back__brand {
    left: 12px;
    top: 42px;
    flex-direction: column;
    gap: 4px;
  }
  .back__brand .brand-mark__dot { width: 14px; height: 14px; }
  .back__brand .brand-mark__name { font-size: 17px; color: #000; }

  .back__title {
    position: absolute;
    left: 122px;
    top: 24px;
    margin: 0;
    font-family: "Cormorant Garamond", "Georgia", serif;
    font-style: italic;
    font-weight: 700;
    font-size: 23px;
    color: #000;
    white-space: nowrap;
  }
  .credentials {
    position: absolute;
    left: 164px;
    top: 89px;
    margin: 0;
    padding: 0 0 0 18px;
    font-size: 17px;
    line-height: 24px;
    color: var(--script-ink);
  }
  .credentials li::marker { color: #000; }
</style>
</head>
<body>
<main class="canvas">

  <section class="card card--front" aria-label="Card front">
    <div class="front__lower"></div>
    <svg class="front__wedge" width="101" height="120" viewBox="0 0 101 120" aria-hidden="true">
      <polygon points="0,0 101,59 0,120" fill="var(--teal)" stroke="#111" stroke-width="1"/>
    </svg>

    <div class="brand-mark front__brand">
      <span class="brand-mark__dot"></span>
      <span class="brand-mark__name">Corinne Dalby</span>
    </div>

    <h1 class="front__title script">Corinne Dalby Nutrition &amp; Fitness</h1>
    <p class="front__role script">Coach for Seniors</p>

    <div class="front__gym plain">
      <span>Private gym at :</span>
      <span>17 Fennick Street,<br>Brantwood, Perth,<br>WA 6291</span>
    </div>

    <div class="front__contact plain">
      Mob : 0412736158<br>
      Email : corinnedalby@fernpost.example
    </div>

    <p class="front__tagline script">For Seniors by a Senior..!</p>
  </section>

  <section class="card card--back" aria-label="Card back">
    <div class="brand-mark back__brand">
      <span class="brand-mark__dot"></span>
      <span class="brand-mark__name">Corinne Dalby</span>
    </div>

    <h2 class="back__title">Corinne Dalby Nutrition &amp; Fitness</h2>

    <ul class="credentials script">
      <li>B.A. ( Soc.) Dip. Ed. (Sec.)</li>
      <li>Wellness Coach Certified for Personal Trainer</li>
      <li>Certified Nutritition</li>
      <li>MOVE ON Facilitator</li>
      <li>Ageing Well Moving Freely</li>
      <li>Facilitator NLP Master</li>
    </ul>
  </section>

</main>
</body>
</html>
```